Specialised investor in e-mobility and energy wants business card design

We need a business card design that fits our existing corporate design. <The look and feel must be 'sharp'/'clean', dynamic, communicate momentum, professionalism etc (as one would imagine from a firm in the financial sector). We like the idea of a reverse-side of the card that includes the logo, and the name and contact details on the other. We expect the deliverable to be whatever format might be required to be able to get cards printed directly by a service such as marlo cards. Our website is www.obrel.finance

```html
<!DOCTYPE html>
<html lang="en">
<head>
<meta charset="utf-8">
<title>Obrel Finance – Business Card</title>
<link href="https://fonts.googleapis.com/css2?family=Bebas+Neue&family=Arimo:wght@400&display=swap" rel="stylesheet">
<style>
  :root {
    --canvas: #161616;
    --card-green: #7bab40;
    --card-dark: #292929;
    --edge-green: #6c9d36;
    --ink: #ffffff;
  }
  * { box-sizing: border-box; margin: 0; padding: 0; }
  html, body { width: 1200px; height: 963px; overflow: hidden; }
  body {
    background: var(--canvas);
    display: flex;
    flex-direction: column;
    align-items: center;
    justify-content: center;
    gap: 56px;
    font-family: "Arimo", Arial, sans-serif;
    color: var(--ink);
  }
  .card {
    position: relative;
    width: 620px;
    height: 354px;
    border-radius: 26px;
  }
  .card--front { background: var(--card-green); }
  .card--back {
    background: var(--card-dark);
    border-bottom: 4px solid var(--edge-green);
    display: flex;
    align-items: center;
    justify-content: center;
  }
  .holder-name {
    position: absolute;
    left: 58px;
    top: 132px;
    font-family: "Bebas Neue", "Oswald", sans-serif;
    font-size: 54px;
    letter-spacing: 0.5px;
    line-height: 1;
  }
  .divider {
    position: absolute;
    left: 352px;
    top: 120px;
    width: 1px;
    height: 78px;
    background: var(--ink);
    opacity: 0.85;
  }
  .contact-list {
    position: absolute;
    left: 372px;
    top: 124px;
    list-style: none;
    font-size: 15px;
    line-height: 24px;
  }
  .contact-list li { display: flex; align-items: center; gap: 9px; }
  .contact-list svg { width: 14px; height: 14px; flex: none; }
  .location {
    position: absolute;
    left: 210px;
    top: 250px;
    font-size: 15px;
  }
  .wordmark { font-family: "Arimo", Arial, sans-serif; font-weight: 400; color: var(--ink); white-space: nowrap; }
  .wordmark--small {
    position: absolute;
    right: 44px;
    bottom: 34px;
    font-size: 24px;
  }
  .wordmark--large { font-size: 56px; letter-spacing: 1px; }
</style>
</head>
<body>
  <section class="card card--front" aria-label="Card front">
    <h1 class="holder-name">Aldo Renwick</h1>
    <div class="divider"></div>
    <ul class="contact-list">
      <li>
        <svg viewBox="0 0 16 16" aria-hidden="true"><path fill="#fff" d="M4.2 1.5 6 4.6 4.7 6a8.5 8.5 0 0 0 5.3 5.3l1.4-1.3 3.1 1.8-.8 2.6c-.2.6-.8.9-1.4.8C6.6 14.4 1.6 9.4.8 3.7.7 3.1 1 2.5 1.6 2.3z"/></svg>
        +41 79 555 0148
      </li>
      <li>
        <svg viewBox="0 0 16 16" aria-hidden="true"><rect x="1" y="3" width="14" height="10" fill="#fff"/><path d="M1 3.5 8 9l7-5.5" fill="none" stroke="#7bab40" stroke-width="1.4"/></svg>
        aldo@obrel.finance
      </li>
      <li>
        <svg viewBox="0 0 16 16" aria-hidden="true"><circle cx="8" cy="8" r="6.5" fill="none" stroke="#fff" stroke-width="1.6"/><path d="M1.5 8h13M8 1.5c-3 3.5-3 9.5 0 13M8 1.5c3 3.5 3 9.5 0 13" fill="none" stroke="#fff" stroke-width="1.2"/></svg>
        www.obrel.finance
      </li>
    </ul>
    <p class="location">Switzerland</p>
    <p class="wordmark wordmark--small">Obrel Finance</p>
  </section>

  <section class="card card--back" aria-label="Card back">
    <p class="wordmark wordmark--large">Obrel Finance</p>
  </section>
</body>
</html>
```